Therapist website

I need a sqaure space web design for my therapy practice. I need a home page, a services page with 4 subpages, an about me, an insurnace page, a contact page, an EMDR page

```html
<!DOCTYPE html>
<html lang="en">
<head>
<meta charset="utf-8">
<title>Willowmere Family Counseling</title>
<link rel="stylesheet" href="https://fonts.googleapis.com/css2?family=Montserrat:wght@400;500;600;700&display=swap">
<style>
:root{
  --teal:#2aa3aa;
  --teal-dark:#1f858c;
  --teal-band:rgba(24,120,128,.82);
  --ink:#3a3a3a;
  --text:#555;
  --nav-bg:#f1f1f1;
  --footer:#3b3b3b;
  --footer-bottom:#2b2b2b;
  --white:#fff;
}
*{box-sizing:border-box;margin:0;padding:0}
html,body{width:1200px;height:3114px;overflow:hidden}
body{position:relative;background:var(--white);font-family:'Montserrat',sans-serif;color:var(--text)}
.abs{position:absolute}
.btn{position:absolute;display:flex;align-items:center;justify-content:center;gap:10px;background:var(--teal);color:#fff;font-weight:700;font-size:14px;letter-spacing:.3px;border-radius:24px;text-transform:uppercase}
/* header */
.top-line{left:0;top:0;width:1200px;height:5px;background:var(--teal)}
.brand{left:98px;top:52px;display:flex;align-items:center;gap:14px}
.brand-dot{width:34px;height:34px;border-radius:50%;background:var(--teal)}
.brand-name{font-size:34px;font-weight:700;color:var(--teal-dark);letter-spacing:1px}
.contact-top{top:28px;right:98px;display:flex;align-items:center;gap:14px;font-size:12px;color:var(--teal-dark)}
.contact-top span{display:flex;align-items:center;gap:6px}
.contact-top .sep{width:1px;height:26px;background:#bbb}
.schedule{left:888px;top:79px;width:212px;height:41px}
.nav{left:0;top:145px;width:1200px;height:48px;background:var(--nav-bg);border-top:1px solid #e2e2e2}
.nav ul{list-style:none;position:absolute;left:98px;top:0;width:960px;height:48px;display:flex;align-items:center;justify-content:space-between;font-size:12px;color:#666}
.nav li.active{color:var(--teal-dark);font-weight:600}
.nav .search{position:absolute;left:1082px;top:14px}
/* hero */
.hero{left:0;top:193px;width:1200px;height:571px;background:linear-gradient(120deg,#7fae5c 0%,#c99a7a 35%,#e2b9a0 55%,#7fb8c0 80%,#9fc67a 100%)}
.hero-box{left:98px;top:498px;width:369px;height:193px;background:rgba(42,163,170,.85);padding:22px 22px;color:#fff}
.hero-box h1{font-size:27px;line-height:32px;font-weight:700;text-transform:uppercase}
.hero-box p{font-size:10.5px;line-height:16px;margin-top:8px}
.hero-box .ghost{position:absolute;left:22px;top:142px;width:116px;height:34px;border:2px solid #fff;border-radius:18px;display:flex;align-items:center;justify-content:center;font-size:11px;font-weight:700}
/* welcome */
.section-title{width:1200px;left:0;text-align:center;font-size:30px;font-weight:600;color:var(--ink);text-transform:uppercase}
.welcome-text{left:100px;top:876px;width:1000px;text-align:center;font-size:12.5px;line-height:21px;color:#444}
.contact-now{left:519px;top:986px;width:160px;height:40px}
/* about */
.photo-family{left:98px;top:1158px;width:317px;height:436px;background:linear-gradient(160deg,#c98b3b,#6b7a3a 55%,#3d4a2a)}
.about-box{left:442px;top:1082px;width:318px;height:417px;background:var(--teal);color:#fff;text-align:center;padding:30px 22px}
.about-box h2{font-size:30px;font-weight:600}
.about-box p{font-size:11.5px;line-height:22px;margin-top:12px}
.about-box .ghost{position:absolute;left:99px;top:342px;width:120px;height:36px;border:2px solid #fff;border-radius:18px;display:flex;align-items:center;justify-content:center;font-size:11px;font-weight:700}
.photo-field{left:783px;top:1158px;width:317px;height:436px;background:linear-gradient(180deg,#d9e4ec 0%,#e8eaea 45%,#c8b07a 70%,#a48a4e 100%)}
.heal{left:430px;top:1530px;width:342px;text-align:center;font-size:15px;line-height:21px;font-weight:700;color:var(--ink)}
.call-btn{left:502px;top:1582px;width:195px;height:38px;font-size:16px}
/* services */
.services{left:0;top:1698px;width:1200px;height:530px;background:linear-gradient(170deg,#6f9b6d,#a5b78b 55%,#86a76e)}
.services-overlay{left:0;top:1698px;width:1200px;height:530px;background:var(--teal-band)}
.services h2,.services-title{color:#fff}
.svc{width:300px;text-align:center;color:#fff}
.svc .ring{width:174px;height:174px;border:4px solid #fff;border-radius:50%;margin:0 auto;display:flex;align-items:center;justify-content:center}
.svc h3{margin-top:26px;font-size:23px;font-weight:600;text-transform:uppercase}
.svc p{font-size:12px;line-height:20px;margin:10px auto 0;width:270px}
.svc .more{width:30px;height:30px;border-radius:50%;background:#fff;margin:20px auto 0;display:flex;align-items:center;justify-content:center}
/* blog */
.card{width:266px;height:310px;background:#f3f3f3;box-shadow:0 6px 10px rgba(0,0,0,.08)}
.card .img{height:150px}
.card .date{position:absolute;right:10px;top:10px;width:52px;height:52px;border-radius:50%;background:var(--teal);color:#fff;font-size:11px;font-weight:700;line-height:14px;text-align:center;padding-top:12px}
.card h4{margin:20px 14px 0;font-size:13.5px;font-weight:600;color:var(--teal);text-transform:uppercase}
.card p{margin:8px 14px 0;font-size:11px;line-height:18px;color:#666}
.card .read{margin:8px 14px 0;font-size:10.5px;font-weight:700;color:var(--teal);text-transform:uppercase}
/* footer */
.footer{left:0;top:2753px;width:1200px;height:299px;background:var(--footer);color:#ddd}
.footer h5{position:absolute;top:38px;font-size:17px;font-weight:600;color:#fff;text-transform:uppercase}
.sitemap{position:absolute;left:100px;top:84px;width:196px;list-style:none;font-size:12.5px}
.sitemap li{height:36px;display:flex;align-items:center;justify-content:space-between;border-bottom:1px solid #5c5c5c}
.quote{position:absolute;left:400px;top:86px;width:410px;font-size:13.5px;line-height:23px}
.quote .by{margin-top:10px}
.arrows{position:absolute;left:718px;top:206px;display:flex;gap:6px}
.arrows span{width:30px;height:30px;border:1px solid #999;border-radius:50%;display:flex;align-items:center;justify-content:center}
.f-contact{position:absolute;left:860px;top:86px;font-size:13.5px;line-height:23px}
.f-contact div{display:flex;gap:14px;margin-bottom:22px}
.socials{display:flex;gap:16px;margin-top:8px}
.socials span{width:20px;height:20px;border-radius:50%;background:#888}
.footer-bottom{left:0;top:3052px;width:1200px;height:62px;background:var(--footer-bottom);color:#bbb;font-size:11.5px}
.footer-bottom p{position:absolute;left:100px;top:24px}
.footer-bottom .up{position:absolute;left:1070px;top:14px;width:32px;height:32px;border:1px solid #888;border-radius:50%;display:flex;align-items:center;justify-content:center}
</style>
</head>
<body>

<header>
  <div class="abs top-line"></div>
  <div class="abs brand"><span class="brand-dot"></span><span class="brand-name">WILLOWMERE</span></div>
  <div class="abs contact-top">
    <span><svg width="14" height="14" viewBox="0 0 24 24"><path fill="#1f858c" d="M6.6 10.8a15 15 0 0 0 6.6 6.6l2.2-2.2c.3-.3.7-.4 1-.2 1.1.4 2.3.6 3.6.6.6 0 1 .4 1 1V20c0 .6-.4 1-1 1A17 17 0 0 1 3 4c0-.6.4-1 1-1h3.5c.6 0 1 .4 1 1 0 1.3.2 2.5.6 3.6.1.3 0 .7-.2 1z"/></svg>123-465-798</span>
    <i class="sep"></i>
    <span><svg width="14" height="11" viewBox="0 0 14 11"><rect x=".5" y=".5" width="13" height="10" fill="none" stroke="#1f858c"/><path d="M.5.5 7 6l6.5-5.5" fill="none" stroke="#1f858c"/></svg>info@willowmere</span>
  </div>
  <div class="btn schedule">Schedule Appointment</div>
  <nav class="abs nav">
    <ul>
      <li class="active">HOME</li><li>|</li><li>SERVICES</li><li>|</li><li>ABOUT ME</li><li>|</li><li>INSURANCE</li><li>|</li><li>EMDR</li><li>|</li><li>CONTACT</li>
    </ul>
    <svg class="search" width="18" height="18" viewBox="0 0 18 18"><circle cx="7" cy="7" r="5.5" fill="none" stroke="#1f858c" stroke-width="2.2"/><path d="M11 11l5.5 5.5" stroke="#1f858c" stroke-width="2.6"/></svg>
  </nav>
</header>

<section>
  <div class="abs hero" role="img" aria-label="Photo of a smiling family of four embracing outdoors"></div>
  <div class="abs hero-box">
    <h1>Leading the way in family counselling</h1>
    <p>Problems that affect our mental health can be just as debilitating as physical illnesses and at times even more so.</p>
    <div class="ghost">LEARN MORE</div>
  </div>
</section>

<section>
  <h2 class="abs section-title" style="top:812px">Welcome to Willowmere</h2>
  <p class="abs welcome-text">Lorem Ipsum is simply dummy text of the printing and typesetting industry. Lorem Ipsum has been the industry's standard dummy text ever since the 1500s, when an unknown printer took a galley of type and scrambled it to make a type specimen book. It has survived not only five centuries, but also the leap into electronic typesetting, remaining essentially unchanged. It was popularised in the 1960s with the release of Letraset sheets containing Lorem Ipsum passages, and more recently with desktop publishing software like Aldus PageMaker including versions of Lorem Ipsum.</p>
  <div class="btn contact-now">Contact Now</div>
</section>

<section>
  <div class="abs photo-family" role="img" aria-label="Photo of a family hugging in an autumn park"></div>
  <div class="abs about-box">
    <h2>ABOUT ME</h2>
    <p>Lorem Ipsum is simply dummy text of the printing and typesetting industry. Lorem Ipsum has been the industry's standard dummy text ever since the 1500s, when an unknown printer took a galley of type and scrambled it to make a type specimen book. It has survived not only five centuries, but also the leap into electronic typesetting, remaining essentially unchanged. It was popularised in the 1960s with the release of Letraset sheets containing Lorem Ipsum</p>
    <div class="ghost">LEARN MORE</div>
  </div>
  <div class="abs photo-field" role="img" aria-label="Photo of a woman with raised arms in a wheat field"></div>
  <p class="abs heal">HEAL THE CORE OF YOUR ADDICTION.<br>CALL NOW</p>
  <div class="btn call-btn"><svg width="16" height="16" viewBox="0 0 24 24"><path fill="#fff" d="M6.6 10.8a15 15 0 0 0 6.6 6.6l2.2-2.2c.3-.3.7-.4 1-.2 1.1.4 2.3.6 3.6.6.6 0 1 .4 1 1V20c0 .6-.4 1-1 1A17 17 0 0 1 3 4c0-.6.4-1 1-1h3.5c.6 0 1 .4 1 1 0 1.3.2 2.5.6 3.6.1.3 0 .7-.2 1z"/></svg>123-456-798</div>
</section>

<section>
  <div class="abs services" role="img" aria-label="Photo of a mother and child playing in a green field"></div>
  <div class="abs services-overlay"></div>
  <h2 class="abs section-title services-title" style="top:1742px">Services</h2>
  <div class="abs svc" style="left:74px;top:1817px">
    <div class="ring"><svg width="80" height="80" viewBox="0 0 80 80"><path d="M28 12 48 20v18c0 14-9 24-20 28C17 62 8 52 8 38V20z" fill="none" stroke="#fff" stroke-width="4"/><path d="M28 26v24M16 38h24" stroke="#fff" stroke-width="6"/><circle cx="60" cy="26" r="7" fill="#fff"/><rect x="52" y="36" width="16" height="30" rx="4" fill="#fff"/></svg></div>
    <h3>Insurance</h3>
    <p>Lorem Ipsum is simply dummy text of the printing and typesetting industry. Lorem Ipsum has been the industry's standard</p>
    <div class="more"><svg width="12" height="8" viewBox="0 0 12 8"><path d="M1 1l5 5 5-5" fill="none" stroke="#1f858c" stroke-width="2.4"/></svg></div>
  </div>
  <div class="abs svc" style="left:448px;top:1817px">
    <div class="ring"><svg width="96" height="60" viewBox="0 0 96 60"><path d="M4 30C18 10 34 4 48 4s30 6 44 26C78 50 62 56 48 56S18 50 4 30z" fill="#fff"/><circle cx="48" cy="30" r="16" fill="#1f858c"/><circle cx="48" cy="30" r="7" fill="#fff"/></svg></div>
    <h3>EMDR</h3>
    <p>Lorem Ipsum is simply dummy text of the printing and typesetting industry. Lorem Ipsum has been the industry's standard</p>
    <div class="more"><svg width="12" height="8" viewBox="0 0 12 8"><path d="M1 1l5 5 5-5" fill="none" stroke="#1f858c" stroke-width="2.4"/></svg></div>
  </div>
  <div class="abs svc" style="left:821px;top:1817px">
    <div class="ring"><svg width="84" height="70" viewBox="0 0 84 70"><circle cx="20" cy="14" r="9" fill="#fff"/><circle cx="64" cy="14" r="9" fill="#fff"/><circle cx="42" cy="28" r="9" fill="#fff"/><rect x="8" y="26" width="24" height="26" rx="4" fill="#fff"/><rect x="52" y="26" width="24" height="26" rx="4" fill="#fff"/><rect x="30" y="40" width="24" height="28" rx="4" fill="#fff"/></svg></div>
    <h3>Consulting Suites</h3>
    <p>Lorem Ipsum is simply dummy text of the printing and typesetting industry. Lorem Ipsum has been the industry's</p>
    <div class="more"><svg width="12" height="8" viewBox="0 0 12 8"><path d="M1 1l5 5 5-5" fill="none" stroke="#1f858c" stroke-width="2.4"/></svg></div>
  </div>
</section>

<section>
  <h2 class="abs section-title" style="top:2288px">Recent Blog</h2>
  <article class="abs card" style="left:150px;top:2358px">
    <div class="img" role="img" aria-label="Photo of a child jumping in a grassy meadow" style="background:linear-gradient(180deg,#eef2f4 55%,#7fae4e)"></div>
    <div class="date">25<br>SEP</div>
    <h4>Lorem Ipsum is dummy</h4>
    <p>Lorem Ipsum is simply dummy text of the printing and typesetting industry. Lorem Ipsum has been the industry.</p>
    <div class="read">Read more &gt;&gt;</div>
  </article>
  <article class="abs card" style="left:457px;top:2358px">
    <div class="img" role="img" aria-label="Photo of a woman using a laptop on the grass" style="background:linear-gradient(180deg,#a9cde8 40%,#6ea040)"></div>
    <div class="date">23<br>OCT</div>
    <h4>Lorem Ipsum is dummy</h4>
    <p>Lorem Ipsum is simply dummy text of the printing and typesetting industry. Lorem Ipsum has been the industry.</p>
    <div class="read">Read more &gt;&gt;</div>
  </article>
  <article class="abs card" style="left:764px;top:2358px">
    <div class="img" role="img" aria-label="Photo of a mother and daughter leaning on a fence" style="background:linear-gradient(180deg,#b7cfe0 30%,#6a4f5a 60%,#5c7a3a)"></div>
    <div class="date">26<br>NOV</div>
    <h4>Lorem Ipsum is dummy</h4>
    <p>Lorem Ipsum is simply dummy text of the printing and typesetting industry. Lorem Ipsum has been the industry.</p>
    <div class="read">Read more &gt;&gt;</div>
  </article>
</section>

<footer>
  <div class="abs footer">
    <h5 style="left:100px">Site Map</h5>
    <ul class="sitemap">
      <li>HOME<span>+</span></li><li>SERVICES<span>+</span></li><li>ABOUT ME<span>+</span></li><li>INSURANCE<span>+</span></li><li>CONTACT ME<span>+</span></li>
    </ul>
    <h5 style="left:400px">Testimonials</h5>
    <div class="quote">
      <p>"Lorem Ipsum is simply dummy text of the printing and typesetting industry. Lorem Ipsum has been the industry's standard dummy text to make a type specimen book. versions of Lorem Ipsum."</p>
      <p class="by">"- Dana Corwell</p>
    </div>
    <div class="arrows">
      <span><svg width="8" height="12" viewBox="0 0 8 12"><path d="M6 1 1 6l5 5" fill="none" stroke="#bbb" stroke-width="2"/></svg></span>
      <span><svg width="8" height="12" viewBox="0 0 8 12"><path d="M2 1l5 5-5 5" fill="none" stroke="#bbb" stroke-width="2"/></svg></span>
    </div>
    <h5 style="left:860px">Contact Us</h5>
    <div class="f-contact">
      <div><svg width="14" height="20" viewBox="0 0 14 20"><path d="M7 0a7 7 0 0 1 7 7c0 5-7 13-7 13S0 12 0 7a7 7 0 0 1 7-7z" fill="#fff"/><circle cx="7" cy="7" r="2.6" fill="#3b3b3b"/></svg><span>123 street name, city name,<br>country name</span></div>
      <div><svg width="16" height="16" viewBox="0 0 24 24"><path fill="#fff" d="M6.6 10.8a15 15 0 0 0 6.6 6.6l2.2-2.2c.3-.3.7-.4 1-.2 1.1.4 2.3.6 3.6.6.6 0 1 .4 1 1V20c0 .6-.4 1-1 1A17 17 0 0 1 3 4c0-.6.4-1 1-1h3.5c.6 0 1 .4 1 1 0 1.3.2 2.5.6 3.6.1.3 0 .7-.2 1z"/></svg><span>123-456-789</span></div>
      <div class="socials"><span></span><span></span><span></span><span></span></div>
    </div>
  </div>
  <div class="abs footer-bottom">
    <p>All Rights Reserved by willowmere © 2018</p>
    <div class="up"><svg width="12" height="8" viewBox="0 0 12 8"><path d="M1 7l5-5 5 5" fill="none" stroke="#bbb" stroke-width="2"/></svg></div>
  </div>
</footer>

</body>
</html>
```